Ordnerdesign für Experte für Versicherungs - und Haftungsfragen im Etiketten - und Verpackungsdruck
Ordnerdesign für Experte für Versicherungs - und Haftungsfragen im Etiketten - und Verpackungsdr..
Zielgruppe
Ich bin Henrik Wallmoser Experte für Versicherungs - und Haftungsfragen im Etiketten - und Verpackungsdruck (meine CI Farben sind orange /schwarz ) Meine Company und das Produkt ist die tarvolink und der tarvolnk Schutzbrief für Druckerereien (schwarz/gelb)
Aufgabenstellung
Gesucht wird für mein/unser Projekt : Ordnerdesign PLUS Register eines Notfallhandbuchs für Unternehmer . Es gibt zwei Produktlinien - zu beiden ist jeweils der Farbfächer /Broschüre beigefügt : Entweder der Notfallordner soll unter ' Henrik Wallmoser Experte für Haftungsfragen .. ( Orange Schwarz oder die Farben meiner Company ( tarvolink Schwarz - gelb ) siehe Broschüre angelegt werden. freie Hand , was also besser passt .

```html
<!DOCTYPE html>
<html lang="de">
<head>
<meta charset="utf-8">
<title>Henrik Wallmoser – Ordner Innenseite</title>
<link rel="stylesheet" href="https://fonts.googleapis.com/css2?family=Montserrat:wght@300&display=swap">
<style>
  :root {
    --stage: #dedede;
    --board-light: #5e5e5e;
    --board-dark: #1f1f1f;
    --board-inner: #262626;
    --spine: #2c2c2c;
    --brand-orange: #e0421c;
    --brand-orange-deep: #c93612;
  }
  html, body {
    margin: 0;
    width: 1200px;
    height: 733px;
    overflow: hidden;
    background: var(--stage);
  }
  .folder-spread {
    position: absolute;
    left: 190px;
    top: 86px;
    width: 820px;
    height: 560px;
    display: flex;
    box-shadow: 0 14px 30px rgba(0,0,0,0.18);
  }
  .panel {
    position: relative;
    width: 405px;
    height: 560px;
  }
  .panel--left {
    background: linear-gradient(135deg, var(--board-light) 0%, var(--board-dark) 65%);
  }
  .spine {
    width: 10px;
    height: 560px;
    background: var(--spine);
    border-left: 1px solid #3a3a3a;
    border-right: 1px solid #1a1a1a;
    box-sizing: border-box;
  }
  .panel--right {
    background: var(--board-inner);
  }
  .owner-name {
    position: absolute;
    left: 90px;
    top: 150px;
    margin: 0;
    font-family: "Montserrat", sans-serif;
    font-weight: 300;
    font-size: 24px;
    letter-spacing: 0.04em;
    color: var(--brand-orange);
  }
  .owner-name__mark {
    display: inline-block;
    width: 10px;
    height: 10px;
    border-radius: 50%;
    background: var(--brand-orange);
    margin-left: 10px;
    vertical-align: middle;
  }
  .pockets {
    position: absolute;
    inset: 0;
  }
</style>
</head>
<body>
  <div class="folder-spread">
    <section class="panel panel--left">
      <p class="owner-name">Henrik Wallmoser<span class="owner-name__mark"></span></p>
    </section>
    <div class="spine"></div>
    <section class="panel panel--right">
      <svg class="pockets" width="405" height="560" viewBox="0 0 405 560">
        <path class="pocket pocket--side" fill="var(--brand-orange-deep)"
              d="M255 560 L255 150 Q255 60 345 60 L405 60 L405 560 Z"/>
        <path class="pocket pocket--bottom" fill="var(--brand-orange)"
              d="M0 560 L0 400 Q30 330 110 335 Q170 340 215 370 L405 370 L405 560 Z"/>
        <path class="pocket-edge" fill="none" stroke="#b5300f" stroke-width="1.2"
              d="M0 400 Q30 330 110 335 Q170 340 215 370 L405 370"/>
      </svg>
    </section>
  </div>
</body>
</html>
```